Family business needs stationery redesign with new logo

Family owned company, established in 1987 wanting a brand 'refresh'. We are an electrical, refrigeration and construction company based in the Barkly Region Northern Territory, Australia. We have a new logo we would like to use which is uploaded along with our current letterhead and email signature. We are also dropping the word 'contractors' so please do not include this on any designs. Please note also, the 'orange' color used in our logo and designs should be Northern Territory red ochre which is as follows:

RGB (Hex): #C75B12
PantoneĀ® 159 C
CMYK: 1 / 74 / 100 / 7

We are needing our stationery redesigned using our new logo. Please include letterheads, business cards, envelopes, and email signatures.

We currently use our business letterheads for quotations, invoices, letters, HR matters, and internal memos.

We also need a separate simplified letterhead for internal paperwork such as employee leave forms, meeting agendas, and meeting minutes etc.
Updates

Reason: Needing more submissions of full package designs. We are wanting all our stationery, including business cards, letterheads, email signatures, envelopes, etc to be cohesive. We also require ALL the information, as supplied on our template letterhead, to be included on the new letterhead designs. including electrical license no.etc Thank you, K&M

Reason: needing more time as work has got in the way of looking over designs. A lot of designs not meeting the brief/criteria.

Industry/Entity Type

Business

Colors
0355a3
f37122

Requirements
Must have
• The 'orange' color used in the designs should be Northern Territory red ochre which is as follows:
• RGB (Hex): #C75B12
• PantoneĀ® 159 C
• CMYK: 1 / 74 / 100 / 7
• ***MUST INCLUDE ALL INFORMATION THAT IS ON OUR CURRENT LETTERHEAD***
Should not have
• Please do not include the word 'contractors'

```html
<!DOCTYPE html>
<html lang="en">
<head>
<meta charset="utf-8">
<title>K&amp;M Stationery Suite</title>
<link href="https://fonts.googleapis.com/css2?family=Arimo:wght@400;700&display=swap" rel="stylesheet">
<style>
  :root{
    --navy:#1b3370;
    --ochre:#c75b12;
    --paper:#ffffff;
    --stage:#b3b3b3;
    --ink:#1a1a1a;
    --muted:#555;
  }
  *{margin:0;padding:0;box-sizing:border-box}
  html,body{width:1200px;height:539px;overflow:hidden;background:var(--stage)}
  body{position:relative;font-family:"Arimo",Arial,sans-serif;color:var(--ink)}
  .sheet{position:absolute;overflow:hidden;background:var(--paper)}
  .sheet--navy{background:var(--navy)}
  .brand{position:absolute;display:flex;align-items:center;gap:0.25em;transform:translate(-50%,-50%);
    font-family:"Arimo",Arial,sans-serif;font-weight:700;color:var(--navy);white-space:nowrap;line-height:1}
  .brand--light{color:var(--paper)}
  .brand__dot{width:0.32em;height:0.32em;border-radius:50%;background:var(--ochre)}
  .bands{position:absolute;left:0;width:100%}
  .contact{position:absolute;font-size:7.4px;line-height:1}
  .contact__row{display:flex;align-items:center;gap:5px;height:10px}
  .icon{width:7px;height:7px;flex:none}
  .icon--dot{border-radius:50%;background:var(--navy)}
  .icon--mail{border:1.2px solid var(--navy)}
  .icon--web{border-radius:50%;border:1.5px solid var(--navy)}
  .sheet--navy .icon--dot{background:var(--paper)}
  .sheet--navy .icon--mail,.sheet--navy .icon--web{border-color:var(--paper)}

  /* letterhead */
  .letterhead{left:27px;top:16px;width:357px;height:506px}
  .letterhead__address{position:absolute;left:15px;top:22px;font-size:7.4px;line-height:9px}
  .letterhead .contact{left:15px;top:44px}
  .letterhead__rule{position:absolute;left:0;top:91px;width:100%;height:5px;background:var(--navy)}
  .letter{position:absolute;left:12px;top:127px;width:335px;font-size:6.9px;line-height:8.2px}
  .letter p{margin-bottom:8px}
  .letter__signature{width:95px;height:16px;margin-top:12px;background:linear-gradient(90deg,#e6e6e6,#f4f4f4);border-radius:3px}
  .letter__signer{color:var(--muted);margin-top:4px;font-size:6.4px}

  /* business card */
  .card-front{left:395px;top:19px;width:200px;height:121px}
  .card-front__name{position:absolute;right:121px;top:78px;text-align:right;font-weight:700;color:var(--navy);font-size:8px}
  .card-front__title{display:block;font-weight:400;font-size:5px;color:var(--muted);margin-top:2px}
  .card-front .contact{left:88px;top:69px;font-size:6px}
  .card-front .contact__row{height:8.5px;gap:4px}
  .card-front .icon{width:5.5px;height:5.5px}
  .card-back{left:605px;top:19px;width:200px;height:121px}

  /* envelopes */
  .envelope{left:395px;top:153px;width:409px;height:176px}
  .envelope .contact{left:19px;top:98px}
  .envelope .contact__row{height:11px}
  .envelope__address{line-height:9.5px;margin-bottom:4px}
  .envelope-back{left:395px;top:343px;width:409px;height:177px}
  .envelope-back__flap{position:absolute;left:0;top:0;width:100%;height:62px;background:var(--navy);border-radius:0 0 40px 40px}

  /* folder */
  .folder{left:815px;top:16px;width:358px;height:506px;
    background:radial-gradient(ellipse 320px 200px at 360px 170px,rgba(255,255,255,0.08),rgba(255,255,255,0) 70%),var(--navy)}
  .folder__social{position:absolute;left:34px;top:441px;display:flex;gap:5px}
  .folder__social span{width:29px;height:29px;border-radius:4px;background:var(--paper)}
  .folder .contact{left:242px;top:432px;font-size:6px;color:var(--paper)}
  .folder__address{line-height:7px;margin-bottom:3px}
  .folder .contact__row{height:10px;gap:4px}
  .folder .icon{width:6px;height:6px}
</style>
</head>
<body>

<section class="sheet letterhead" aria-label="Letterhead">
  <div class="letterhead__address">14 Ochre Road<br>Tennant Creek NT 0860</div>
  <div class="contact">
    <div class="contact__row"><span class="icon icon--dot"></span>08 8962 4410</div>
    <div class="contact__row"><span class="icon icon--mail"></span>mark.kelly@kmgroup.au</div>
    <div class="contact__row"><span class="icon icon--web"></span>www.kmgroup.au</div>
  </div>
  <div class="brand" style="left:273px;top:48px;font-size:33px">K&amp;M<span class="brand__dot"></span></div>
  <div class="letterhead__rule"></div>
  <div class="letter">
    <p>Your Ref: SP KMC</p>
    <p>1 Dec 2014</p>
    <p style="margin-bottom:22px">Mr Name of client<br>Designantion<br>Dunmore Holdings<br>Level 10<br>Address<br>DARWIN NT 0800</p>
    <p>Thank you for the opportunity of providing a proposal regarding the form and nature of assistance we can provide to you with the development of the Dunmore Holdings website our company commitment to providing innovative online solutions to the web developments required by organisations is the key to our success. We believe the benefits of our methodology and experience with a broad spectrum of web projects puts us in a strong position to assist you.</p>
    <p>We realise the importance of this project to Dunmore Holdings and look forward to the opportunity of contributing and working with you.</p>
    <p>Thank you for the opportunity of providing a proposal regarding the form and nature of assistance we can provide to you with the development of the Dunmore Holdings website our company commitment to providing innovative online solutions to the web developments required by</p>
    <div class="letter__signature" role="img" aria-label="Handwritten signature"></div>
    <div class="letter__signer">Ruth K Moreland</div>
  </div>
  <svg class="bands" style="top:492px;height:14px" viewBox="0 0 357 14" preserveAspectRatio="none">
    <polygon points="0,0 210,0 214,14 0,14" fill="var(--navy)"/>
    <polygon points="212,0 357,0 357,14 216,14" fill="var(--ochre)"/>
  </svg>
</section>

<section class="sheet card-front" aria-label="Business card front">
  <div class="brand" style="left:62px;top:36px;font-size:22px">K&amp;M<span class="brand__dot"></span></div>
  <div class="card-front__name">Mark Kelly<span class="card-front__title">President</span></div>
  <div class="contact">
    <div class="contact__row" style="display:block;height:auto;line-height:7px;margin-bottom:2px">14 Ochre Road<br>Tennant Creek NT 0860</div>
    <div class="contact__row"><span class="icon icon--dot"></span>08 8962 4410</div>
    <div class="contact__row"><span class="icon icon--mail"></span>mark.kelly@kmgroup.au</div>
  </div>
  <svg class="bands" style="top:113px;height:8px" viewBox="0 0 200 8" preserveAspectRatio="none">
    <polygon points="0,0 117,0 119,8 0,8" fill="var(--navy)"/>
    <polygon points="118,0 200,0 200,8 120,8" fill="var(--ochre)"/>
  </svg>
</section>

<section class="sheet sheet--navy card-back" aria-label="Business card back">
  <div class="brand brand--light" style="left:100px;top:60px;font-size:26px">K&amp;M<span class="brand__dot"></span></div>
</section>

<section class="sheet envelope" aria-label="Envelope front">
  <div class="brand" style="left:75px;top:42px;font-size:26px">K&amp;M<span class="brand__dot"></span></div>
  <div class="contact">
    <div class="envelope__address">14 Ochre Road<br>Tennant Creek NT 0860</div>
    <div class="contact__row"><span class="icon icon--dot"></span>08 8962 4410</div>
    <div class="contact__row"><span class="icon icon--mail"></span>mark.kelly@kmgroup.au</div>
    <div class="contact__row"><span class="icon icon--web"></span>www.kmgroup.au</div>
  </div>
  <svg class="bands" style="top:163px;height:13px" viewBox="0 0 409 13" preserveAspectRatio="none">
    <polygon points="0,0 241,0 244,13 0,13" fill="var(--navy)"/>
    <polygon points="243,0 409,0 409,13 246,13" fill="var(--ochre)"/>
  </svg>
</section>

<section class="sheet envelope-back" aria-label="Envelope back">
  <div class="envelope-back__flap"></div>
  <div class="brand brand--light" style="left:205px;top:31px;font-size:22px">K&amp;M<span class="brand__dot"></span></div>
</section>

<section class="sheet sheet--navy folder" aria-label="Presentation folder">
  <div class="brand brand--light" style="left:179px;top:248px;font-size:82px">K&amp;M<span class="brand__dot"></span></div>
  <div class="folder__social" aria-label="Social media links"><span></span><span></span><span></span><span></span></div>
  <div class="contact">
    <div class="folder__address">PO Box 217, Paterson Street,<br>Tennant Creek, NT Australia</div>
    <div class="contact__row"><span class="icon icon--dot"></span>(08) 8962 4410</div>
    <div class="contact__row"><span class="icon icon--mail"></span>(08) 8962 4411</div>
    <div class="contact__row"><span class="icon icon--web"></span>www.kmgroup.au</div>
  </div>
</section>

</body>
</html>
```